Financial Services Company Needs New UI/UX

Hello!

We would like to see some UI/UX ideas for our software platform. I've attached a screen capture of our current "dashboard" (or main home page, essentially). We're looking for a very simple, clean, sleek design as there are many different pages throughout the system that will all need to coordinate. You can also view our website to see the colors and general "look" we have on there. It would be ideal for the portal to coordinate with the website since that is how they access the login page. Please submit your best ideas for the dashboard and we will reach out to our favorite designer to move forward with the rest of the pages. You can find our color hex codes on our website on the "Media" page. Should you need any other supporting logos or files please send us a message and we will try to accommodate.

Thanks!

Website: www.lendmarkbuilt.example

Target Market(s)

Our clients are contractors in the construction industry and our software helps them manage material purchases for their jobs.

Industry/Entity Type

Financial Service

Font styles to use
Sans Serif

Requirements
Must have
• The same content and language as the current dashboard but an updated look.
Should not have
• Too much distraction or busy patterns, we're looking for clean and simple and user friendly. Likely a solid or subtly textured background would be best.

```html
<!DOCTYPE html>
<html lang="en">
<head>
<meta charset="utf-8">
<title>Design Idea 01a – New Dashboard</title>
<link rel="stylesheet" href="https://fonts.googleapis.com/css2?family=Ubuntu:wght@400;500;700&family=Open+Sans:wght@400;600;700&display=swap">
<style>
  :root{
    --stage-dark:#1c1c1e;
    --stage-mid:#2e2e31;
    --title-lilac:#a99cf0;
    --panel:#ffffff;
    --brand-red:#d04a4a;
    --card-blue:#5193d0;
    --bar-dark:#343438;
    --row-lilac:#e7e5f8;
    --row-blush:#ece3e2;
    --head-row:#f5f4f2;
    --head-link:#8a6d4a;
    --rule:#d2d0d4;
    --ink:#222;
    --alert-yellow:#f5b800;
    --info-red:#e8401c;
  }
  *{box-sizing:border-box;margin:0;padding:0}
  html,body{width:1200px;height:1200px;overflow:hidden}
  body{
    position:relative;
    background:radial-gradient(ellipse at 50% 45%, var(--stage-mid) 0%, var(--stage-dark) 75%);
    font-family:"Open Sans",sans-serif;color:var(--ink);
  }
  .board-title,.board-caption{
    position:absolute;left:0;width:1200px;text-align:center;
    font-family:"Ubuntu",sans-serif;color:var(--title-lilac);font-weight:400;
  }
  .board-title{top:74px;font-size:33px;letter-spacing:1px}
  .board-caption{top:908px;font-size:27px}

  .dashboard{position:absolute;left:30px;top:290px;width:1122px;height:588px;background:var(--panel)}
  .dashboard-bar{
    position:absolute;left:16px;top:12px;width:1089px;height:36px;background:var(--brand-red);
    display:flex;align-items:center;padding-left:14px;gap:10px;
    color:#fff;font-family:"Ubuntu",sans-serif;font-weight:700;font-size:15px;letter-spacing:.3px;
  }
  .legend{position:absolute;left:19px;top:50px;display:flex;align-items:center;gap:6px;font-size:11.5px;color:#444}
  .legend .gap{width:8px}
  .icon{display:inline-block;flex:none}

  .summary-card{position:absolute;top:79px;width:234px;height:178px;background:var(--card-blue);border-radius:4px;overflow:hidden;color:#fff;text-align:center}
  .summary-card header{
    height:36px;background:var(--bar-dark);display:flex;align-items:center;justify-content:center;gap:10px;
    font-family:"Ubuntu",sans-serif;font-weight:500;font-size:15.5px;
  }
  .amount{font-family:"Ubuntu",sans-serif;font-weight:700;font-size:24px;margin-top:11px;line-height:1.2}
  .details{font-family:"Ubuntu",sans-serif;font-weight:700;font-size:11px;line-height:13.5px;margin-top:8px}
  .actions{position:absolute;left:0;right:0;bottom:20px;display:flex;justify-content:center;gap:10px}
  .pill{background:#fff;color:var(--ink);border-radius:13px;height:25px;padding:0 9px;display:flex;align-items:center;font-family:"Ubuntu",sans-serif;font-weight:500;font-size:12px}

  .data-panel{position:absolute;top:272px;width:547px}
  .data-panel header{height:37px;background:var(--bar-dark);color:#fff;display:flex;align-items:center;gap:10px;padding-left:14px;font-family:"Ubuntu",sans-serif;font-weight:500;font-size:14px}
  table{width:100%;border-collapse:collapse;table-layout:fixed;font-size:10px}
  th,td{border-right:1px solid var(--rule);text-align:center;vertical-align:middle}
  th:last-child,td:last-child{border-right:none}
  th{height:39px;background:var(--head-row);color:var(--head-link);text-decoration:underline;font-weight:600;font-size:11.5px}
  td{height:32px;line-height:11px;border-bottom:1px solid #fff}
  tbody tr:nth-child(odd){background:var(--row-lilac)}
  tbody tr:nth-child(even){background:var(--row-blush)}
  .data-panel table{border-bottom:1px solid var(--rule)}
</style>
</head>
<body>
  <h1 class="board-title">DESIGN IDEA - 01a</h1>

  <main class="dashboard">
    <div class="dashboard-bar">
      <svg class="icon" width="18" height="18" viewBox="0 0 18 18"><circle cx="9" cy="9" r="9" fill="var(--alert-yellow)"/><text x="9" y="13.5" text-anchor="middle" font-family="Open Sans,sans-serif" font-weight="700" font-size="12" fill="#fff">?</text></svg>
      DASHBOARD
    </div>
    <div class="legend">
      <svg class="icon" width="15" height="13" viewBox="0 0 15 13"><path d="M7.5 0L15 13H0z" fill="var(--alert-yellow)"/><rect x="6.8" y="4" width="1.4" height="5" fill="#222"/><rect x="6.8" y="10" width="1.4" height="1.4" fill="#222"/></svg>
      Indicates an Action is Required
      <span class="gap"></span>
      <svg class="icon" width="16" height="16" viewBox="0 0 16 16"><circle cx="8" cy="8" r="8" fill="var(--alert-yellow)"/><text x="8" y="12" text-anchor="middle" font-family="Open Sans,sans-serif" font-weight="700" font-size="11" fill="#fff">?</text></svg>
      Information only - no action required
    </div>

    <section class="summary-card" style="left:196px">
      <header>
        <svg class="icon" width="17" height="17" viewBox="0 0 17 17"><circle cx="8.5" cy="8.5" r="8.5" fill="var(--info-red)"/><rect x="7.6" y="3.5" width="1.8" height="1.8" fill="#fff"/><rect x="7.6" y="6.6" width="1.8" height="6.5" fill="#fff"/></svg>
        Available Master Credit
      </header>
      <div class="amount">$1,29,500.00</div>
      <div class="details" style="margin-top:14px">Master Credit Limit : 250,000.00</div>
      <div class="actions"><span class="pill">Setup New Job</span></div>
    </section>

    <section class="summary-card" style="left:440px">
      <header>
        <svg class="icon" width="17" height="17" viewBox="0 0 17 17"><circle cx="8.5" cy="8.5" r="8.5" fill="var(--info-red)"/><rect x="7.6" y="3.5" width="1.8" height="1.8" fill="#fff"/><rect x="7.6" y="6.6" width="1.8" height="6.5" fill="#fff"/></svg>
        Last Payment
      </header>
      <div class="amount">$500.00</div>
      <div class="details" style="margin-top:14px">Last Payment Date : 6/28/2016</div>
      <div class="actions"><span class="pill">View Payments</span><span class="pill">View Billings</span></div>
    </section>

    <section class="summary-card" style="left:685px">
      <header>
        <svg class="icon" width="17" height="15" viewBox="0 0 17 15"><path d="M8.5 0L17 15H0z" fill="var(--alert-yellow)"/><rect x="7.7" y="5" width="1.6" height="5.5" fill="#222"/><rect x="7.7" y="11.6" width="1.6" height="1.6" fill="#222"/></svg>
        Next Payment
      </header>
      <div class="amount">$158.95</div>
      <div class="details">Due Date : 6/28/2016<br>Current Principle : $9,968.46<br>Minimum Interest/Fees :&nbsp; $158.95</div>
      <div class="actions"><span class="pill">Make Payment</span></div>
    </section>

    <section class="data-panel" style="left:11px">
      <header>
        <svg class="icon" width="18" height="20" viewBox="0 0 18 20"><rect x="1" y="1" width="16" height="18" rx="2" fill="none" stroke="#e05050" stroke-width="1.6"/><rect x="4.5" y="5" width="9" height="10" fill="none" stroke="#e05050" stroke-width="1"/><path d="M4.5 8.3h9M4.5 11.6h9M7.5 5v10M10.5 5v10" stroke="#e05050" stroke-width="1"/></svg>
        Task Summary
      </header>
      <table>
        <colgroup><col style="width:31px"><col style="width:207px"><col style="width:185px"><col style="width:124px"></colgroup>
        <thead><tr><th></th><th>Task</th><th>Status</th><th>Received</th></tr></thead>
        <tbody>
          <tr>
            <td><svg class="icon" width="16" height="16" viewBox="0 0 16 16"><circle cx="8" cy="8" r="8" fill="var(--alert-yellow)"/><text x="8" y="12" text-anchor="middle" font-family="Open Sans,sans-serif" font-weight="700" font-size="11" fill="#fff">?</text></svg></td>
            <td>Supplier Invoice</td><td>Confirmation by Account Manager<br>Pending</td><td>5/1/2016</td>
          </tr>
          <tr><td></td><td></td><td></td><td></td></tr>
          <tr><td></td><td></td><td></td><td></td></tr>
          <tr><td></td><td></td><td></td><td></td></tr>
          <tr><td></td><td></td><td></td><td></td></tr>
          <tr><td></td><td></td><td></td><td></td></tr>
          <tr><td></td><td></td><td></td><td></td></tr>
        </tbody>
      </table>
    </section>

    <section class="data-panel" style="left:564px">
      <header>
        <svg class="icon" width="18" height="18" viewBox="0 0 18 18"><path d="M3 15L14 4" stroke="var(--alert-yellow)" stroke-width="2.6" stroke-linecap="round"/><path d="M15 15L5 5" stroke="var(--alert-yellow)" stroke-width="2.6" stroke-linecap="round"/><path d="M2 2l5 1-4 4z" fill="var(--alert-yellow)"/><circle cx="14.5" cy="3.5" r="2.6" fill="none" stroke="var(--alert-yellow)" stroke-width="1.8"/></svg>
        Active Jobs
      </header>
      <table>
        <colgroup><col style="width:100px"><col style="width:125px"><col style="width:103px"><col style="width:112px"><col style="width:107px"></colgroup>
        <thead><tr><th>Job#</th><th>Job Name</th><th>Status</th><th>Credit Limit</th><th>Avail. Credit</th></tr></thead>
        <tbody>
          <tr><td>pc101-001</td><td>Job#001</td><td>Active</td><td>$50,100.00</td><td>$35,100.00</td></tr>
          <tr><td>pc101-002</td><td>Job#002</td><td>Active</td><td>$40,000.00</td><td>$2,00.00</td></tr>
          <tr><td>pc101-003</td><td>Job#003</td><td>Active</td><td>$22,000.00</td><td>$0.00</td></tr>
          <tr><td>pc101-004</td><td>Job#004</td><td>Active</td><td>$10,400.00</td><td>$10,400.00</td></tr>
          <tr><td></td><td></td><td></td><td></td><td></td></tr>
          <tr><td></td><td></td><td></td><td></td><td></td></tr>
          <tr><td></td><td></td><td></td><td></td><td></td></tr>
        </tbody>
      </table>
    </section>
  </main>

  <p class="board-caption">New Dashboard</p>
</body>
</html>
```